Postcard for Educational Consultant
Pathways for Fluency in Language Learning
Bridging Languages with Technology
Education
Public schools, private and charter schools, school districts
My logo. Please match colors to it.
Instructions for postcard text.
Photo 1
Photo 2 (purchased from PixVault)
Photo 3 (purchased from PixVault)
Photo 4 (purchased from PixVault)
QR Code
Photo 4

```html
<!DOCTYPE html>
<html lang="en">
<head>
<meta charset="utf-8">
<title>Pathways for Fluency in Language Learning – Postcard</title>
<link href="https://fonts.googleapis.com/css2?family=Open+Sans:wght@400;600;700&display=swap" rel="stylesheet">
<style>
  :root {
    --stage: #e9e7e3;
    --paper: #ffffff;
    --paper-soft: #f3f4f4;
    --ink: #3c3f42;
    --teal-band: #1d6f86;
    --cyan: #1ea2cc;
    --blue-accent: #1f8fc0;
    --green: #79b843;
    --title-bar: #1a86b8;
  }
  * { box-sizing: border-box; margin: 0; padding: 0; }
  html, body { width: 1200px; height: 850px; overflow: hidden; }
  body {
    background: var(--stage);
    font-family: "Open Sans", sans-serif;
    color: var(--ink);
    position: relative;
  }
  .postcard {
    position: absolute;
    top: 223px;
    width: 570px;
    height: 404px;
    background: var(--paper);
    overflow: hidden;
    box-shadow: 0 2px 6px rgba(0,0,0,.18);
  }
  .postcard--front { left: 20px; background: var(--paper-soft); }
  .postcard--back { left: 610px; }

  /* Front */
  .front-photo {
    position: absolute; right: 0; top: 0;
    width: 275px; height: 315px;
    background: linear-gradient(135deg, #b7a89d 0%, #8d7467 40%, #d98fae 80%, #ecc0d2 100%);
  }
  .front-copy {
    position: absolute; left: 22px; top: 92px; width: 262px;
    font-size: 8.2px; line-height: 1.45;
  }
  .front-copy p { margin-bottom: 8px; }
  .front-copy .callout { color: var(--blue-accent); font-weight: 600; font-size: 8.8px; }
  .front-copy ul { list-style: none; }
  .front-copy li { position: relative; padding-left: 10px; margin-bottom: 4px; }
  .front-copy li::before { content: "•"; position: absolute; left: 0; }
  .front-copy .shout { font-weight: 600; }
  .front-band {
    position: absolute; left: 0; bottom: 0; width: 100%; height: 89px;
    background: var(--teal-band); color: #fff;
  }
  .brand {
    position: absolute; display: flex; align-items: center; gap: 8px;
    font-size: 9.5px; line-height: 1.25; font-weight: 600;
  }
  .brand-dot { width: 22px; height: 22px; border-radius: 50%; background: var(--green); flex: none; }
  .front-band .brand { left: 26px; top: 26px; color: #fff; width: 200px; }
  .front-contact {
    position: absolute; left: 300px; top: 24px; font-size: 8px; line-height: 1.5;
    padding-left: 8px; border-left: 1px solid rgba(255,255,255,.6);
  }
  .front-contact .phones { font-size: 10px; font-weight: 600; }
  .stamp-box {
    position: absolute; right: 22px; top: 14px; width: 58px; height: 58px; background: #fff;
  }

  /* Back */
  .back-photo-group {
    position: absolute; left: 0; top: 0; width: 312px; height: 112px;
    background: linear-gradient(90deg, #3a3a3a 0%, #8d8d8d 45%, #5a5a5a 70%, #c9c9c9 100%);
  }
  .back-title-bar {
    position: absolute; left: 112px; top: 20px; width: 200px; height: 42px;
    background: var(--title-bar); color: #fff;
    font-size: 11.5px; line-height: 1.3; font-weight: 600; text-align: right; padding: 5px 10px 0 0;
  }
  .back-photo-boy {
    position: absolute; right: 0; top: 0; width: 258px; height: 290px;
    background: linear-gradient(160deg, #e4e2dd 0%, #cdb49b 40%, #8f6a52 70%, #dedbd5 100%);
  }
  .back-column {
    position: absolute; left: 0; top: 112px; width: 312px; height: 292px;
    background: var(--cyan); color: #fff;
    padding: 16px 18px 0 20px; font-size: 8.3px; line-height: 1.45;
  }
  .back-column p { margin-bottom: 9px; }
  .back-column ul { list-style: none; }
  .back-column li { position: relative; padding-left: 10px; margin-bottom: 2px; }
  .back-column li::before { content: "•"; position: absolute; left: 0; }
  .back-footer { position: absolute; right: 0; top: 290px; width: 258px; height: 114px; background: var(--paper); }
  .back-footer .brand { left: 22px; top: 14px; color: var(--teal-band); width: 200px; }
  .back-url {
    position: absolute; left: 22px; top: 66px; color: var(--green);
    font-size: 11.5px; font-weight: 700;
  }
  .back-phones { position: absolute; left: 22px; top: 84px; font-size: 9px; font-weight: 600; color: var(--ink); }
</style>
</head>
<body>

<section class="postcard postcard--front" aria-label="Postcard front">
  <div class="front-photo" role="img" aria-label="Photo of a worried young girl in a pink top looking over her shoulder in a classroom"></div>
  <div class="front-copy">
    <p>Imagine what it's like to be in a strange country and you don't speak the language. Others stare at you day in/day out. You don't know what they expect of you.</p>
    <p class="callout">. . . and you would do anything not to be in this class in this classroom . . . in this school.</p>
    <ul>
      <li>Be the teacher, the school, the district to empower that child.</li>
      <li>Broaden the learning experiences of all your students by engaging LEP students and their parents in your school community.</li>
      <li>Improve or develop a language program worthy of a national grant.</li>
      <li class="shout">AND DO IT ALL WITH THE RESOURCES YOU ALREADY HAVE!</li>
    </ul>
  </div>
  <div class="front-band">
    <div class="brand"><span class="brand-dot"></span><span>Pathways for Fluency<br>in Language Learning</span></div>
    <div class="front-contact">
      <div>PO Box 42 | Millbrook, VA 24000-0042</div>
      <div class="phones">1-555-014-7020 or 1-555-016-0605</div>
    </div>
    <div class="stamp-box"></div>
  </div>
</section>

<section class="postcard postcard--back" aria-label="Postcard back">
  <div class="back-photo-group" role="img" aria-label="Black and white photos of a teacher working with students"></div>
  <div class="back-title-bar">Bridging Languages<br>with Technology</div>
  <div class="back-photo-boy" role="img" aria-label="Photo of a smiling boy at a computer"></div>
  <div class="back-column">
    <p>Pathways for Fluency in Language Learning offers consulting services and teacher training to schools and districts with emergent ESL populations and/or growing second language programs.</p>
    <p>Pre- and in-service training services as well as consulting services are available both on-site and online. We take special pride in featuring open source (free) software programs for language learning and a hands-on approach to using the software effectively for both instruction and assessment.</p>
    <ul>
      <li>Facilitating the acquisition of English for your LEP students</li>
      <li>Building second language programs for your LEP population</li>
      <li>On-site in-service programs and videoconference workshops for faculty and staff</li>
      <li>Online consulting services for administration and teachers</li>
      <li>On-site consulting for individuals or teams</li>
    </ul>
  </div>
  <div class="back-footer">
    <div class="brand"><span class="brand-dot"></span><span>Pathways for Fluency<br>in Language Learning</span></div>
    <div class="back-url">www.fluencypathways.org</div>
    <div class="back-phones">1-555-014-7020 or 1-555-016-0605</div>
  </div>
</section>

</body>
</html>
```